Company or website name
- zestoplex
- Links to the website
- www.zestoplex.com
- Describe your company and organization and target audience
- I need a website design for a new kids vitamins brand called ZESTOPLEX.   This brand is built on the foundations that it has everything you need, nothing that you dont (e.g. GMO, Animal Content, Soy, Dairy, Gelatin) and is right for everyone. This is a brand that appeals to millenial moms who want only the best for their kids.  It's colorful, bold, vibrant yet credible because all formulas are clinically tested.
- Other Facts

```html
<!DOCTYPE html>
<html lang="en">
<head>
<meta charset="utf-8">
<title>Zestoplex — Making kids healthy and smart</title>
<link rel="stylesheet" href="https://fonts.googleapis.com/css2?family=Montserrat:ital,wght@0,300;0,400;0,500;0,600;0,700;0,800;1,300&display=swap">
<style>
  :root {
    --sky: #5bbde9;
    --white: #ffffff;
    --navy-blue: #1d6e9f;
    --text-blue: #2a7cb2;
    --title-blue: #1f7ab8;
    --teal: #2a8cb5;
    --btn-blue: #1f6fa5;
    --card-pink: #fdeef1;
    --card-blue: #dbeef6;
    --card-cream: #fdf3df;
    --orange-green: #4e9a78;
    --elder-purple: #6f5fa3;
    --berry-red: #d05656;
    --badge-1: #4faa6f;
    --badge-2: #f0a830;
    --badge-3: #2a9aa6;
    --badge-4: #6d59a0;
    --badge-5: #c0478f;
    --badge-6: #e8743a;
    --badge-7: #d9534f;
  }
  * { box-sizing: border-box; margin: 0; padding: 0; }
  html, body { width: 1200px; height: 2345px; overflow: hidden; background: var(--white); }
  body { font-family: "Montserrat", sans-serif; position: relative; color: var(--text-blue); }
  .abs { position: absolute; }

  /* Hero */
  .hero { left: 0; top: 0; width: 1200px; height: 550px; background: var(--sky); overflow: hidden; }
  .brand { left: 119px; top: 22px; font-size: 32px; font-weight: 800; color: var(--white); letter-spacing: 0.5px; }
  .nav { top: 31px; left: 0; width: 1200px; }
  .nav a { position: absolute; color: var(--white); text-decoration: none; font-size: 15px; font-weight: 500; }
  .hero-title { left: 115px; top: 156px; font-size: 58px; line-height: 64px; font-weight: 700; color: var(--white); }
  .hero-btn { left: 117px; top: 377px; width: 155px; height: 38px; border-radius: 19px; background: var(--white); color: var(--title-blue); font-size: 15px; font-weight: 500; display: flex; align-items: center; justify-content: center; }
  .hero-cloud { left: 420px; top: 230px; }
  .hero-bear { left: 720px; top: 112px; width: 410px; height: 268px; border-radius: 180px 180px 40px 40px; background: linear-gradient(170deg, #d9903f 0%, #f0b56a 55%, #f6d7a8 100%); }
  .hero-bottles { left: 540px; top: 378px; width: 630px; height: 172px; border-radius: 14px 14px 0 0; background: linear-gradient(90deg, #3ea57c 0%, #e9b23c 16%, #3aa3c9 32%, #7a67b5 48%, #c452a0 64%, #e8743a 80%, #d85a5a 100%); }

  /* About */
  .section-title { left: 0; width: 1200px; text-align: center; font-weight: 600; color: var(--navy-blue); }
  .about-title { top: 614px; font-size: 40px; }
  .about-lead { top: 675px; left: 0; width: 1200px; text-align: center; font-size: 15.5px; line-height: 1.3; color: var(--text-blue); }
  .card { top: 757px; width: 302px; height: 370px; border-radius: 8px; text-align: center; }
  .card--body { left: 106px; background: var(--card-pink); }
  .card--smart { left: 445px; background: var(--card-blue); }
  .card--mind { left: 784px; background: var(--card-cream); }
  .card-icon { position: absolute; left: 116px; top: 30px; width: 70px; height: 90px; border-radius: 12px; background: linear-gradient(180deg, #2b7fbf, #1d5f96); opacity: 0.85; }
  .card-title { position: absolute; top: 138px; width: 100%; font-size: 24px; font-weight: 500; color: var(--title-blue); }
  .card-text { position: absolute; top: 190px; left: 26px; width: 250px; font-size: 12.5px; line-height: 1.3; color: var(--text-blue); }
  .card-btn { position: absolute; left: 101px; top: 314px; width: 100px; height: 22px; border-radius: 11px; background: var(--btn-blue); color: var(--white); font-size: 10px; font-weight: 600; display: flex; align-items: center; justify-content: center; }

  /* Products */
  .products-title { top: 1204px; font-size: 44px; }
  .products-lead { top: 1262px; left: 0; width: 1200px; text-align: center; font-size: 15.5px; line-height: 1.3; color: var(--text-blue); }
  .product { top: 1346px; width: 340px; text-align: center; }
  .product--orange { left: 77px; }
  .product--elder { left: 427px; }
  .product--berry { left: 773px; }
  .product-bottle { margin: 0 auto; width: 128px; height: 240px; border-radius: 30px 30px 22px 22px; }
  .product--orange .product-bottle { background: linear-gradient(180deg, #3ea57c 0 12%, #f5b04a 12% 55%, #eef2ef 55%); }
  .product--elder .product-bottle { background: linear-gradient(180deg, #7a67b5 0 12%, #d8364e 12% 55%, #eceaf3 55%); }
  .product--berry .product-bottle { background: linear-gradient(180deg, #d85a5a 0 12%, #d8364e 12% 55%, #f3eaea 55%); }
  .product-name { margin-top: 22px; font-size: 31px; font-weight: 400; color: var(--navy-blue); letter-spacing: 0.5px; }
  .product-tag { margin-top: 12px; font-size: 25px; font-weight: 400; color: var(--teal); }
  .product-desc { margin: 10px auto 0; width: 200px; font-size: 15px; line-height: 1.3; color: var(--text-blue); }
  .buy-btn { top: 1781px; width: 104px; height: 40px; border-radius: 4px; color: var(--white); font-size: 16px; display: flex; align-items: center; justify-content: center; }
  .buy-btn--orange { left: 199px; background: var(--orange-green); }
  .buy-btn--elder { left: 545px; background: var(--elder-purple); }
  .buy-btn--berry { left: 891px; background: var(--berry-red); }
  .badges { left: 306px; top: 1852px; }

  /* Contact */
  .contact { left: 0; top: 1960px; width: 1200px; height: 385px; background: var(--sky); }
  .contact-frame { left: 60px; top: 51px; width: 1080px; height: 275px; border: 2px solid var(--white); }
  .contact-divider { left: 601px; top: 51px; width: 2px; height: 275px; background: var(--white); }
  .contact-col { top: 51px; width: 540px; text-align: center; color: var(--white); }
  .contact-col--phone { left: 60px; }
  .contact-col--mail { left: 601px; }
  .contact-icon { position: absolute; left: 244px; top: -26px; width: 52px; height: 52px; border-radius: 50%; background: var(--white); display: flex; align-items: center; justify-content: center; }
  .contact-note { margin-top: 66px; font-size: 15.5px; }
  .contact-main { margin-top: 28px; font-size: 36px; font-weight: 300; font-style: italic; }
  .contact-hours, .contact-time { white-space: pre; font-size: 15px; letter-spacing: 1px; }
  .contact-hours { margin-top: 22px; }
  .contact-time { margin-top: 14px; }
</style>
</head>
<body>

<header class="abs hero">
  <div class="abs brand">ZESTOPLEX</div>
  <nav class="abs nav">
    <a href="#" style="left:714px">Home</a>
    <a href="#" style="left:830px">About</a>
    <a href="#" style="left:945px">Products</a>
    <a href="#" style="left:1075px">Contact</a>
  </nav>
  <svg class="abs hero-cloud" width="780" height="320" viewBox="0 0 780 320" aria-hidden="true">
    <g fill="#ffffff">
      <circle cx="90" cy="260" r="75"/>
      <circle cx="200" cy="180" r="100"/>
      <circle cx="420" cy="150" r="110"/>
      <circle cx="620" cy="120" r="100"/>
      <circle cx="760" cy="140" r="80"/>
      <rect x="60" y="240" width="720" height="80"/>
    </g>
  </svg>
  <div class="abs hero-bear" role="img" aria-label="Illustration of a friendly teddy bear waving"></div>
  <div class="abs hero-bottles" role="img" aria-label="Row of seven colourful gummy vitamin bottles"></div>
  <h1 class="abs hero-title">Making kids<br>healthy and smart</h1>
  <a class="abs hero-btn">Read more</a>
</header>

<main>
  <h2 class="abs section-title about-title">What is Zestoplex?</h2>
  <p class="abs about-lead">This brand is built on the foundations that it has everything you need,<br>nothing that you dont and is right for everyone.<br>This is a brand that appeals to millenial moms who want only the best for their kids.</p>

  <article class="abs card card--body">
    <div class="card-icon" role="img" aria-label="Icon of an active figure"></div>
    <h3 class="card-title">Healthy Body</h3>
    <p class="card-text">Itaque earum rerum hic tenetur a sapiente delectus, ut aut reiciendis voluptatibus maiores alias consequatur aut perferendis doloribus asperiores repellat.</p>
    <a class="card-btn">Read more</a>
  </article>
  <article class="abs card card--smart">
    <div class="card-icon" role="img" aria-label="Icon of a lightbulb idea"></div>
    <h3 class="card-title">Smart</h3>
    <p class="card-text">Itaque earum rerum hic tenetur a sapiente delectus, ut aut reiciendis voluptatibus maiores alias consequatur aut perferendis doloribus asperiores repellat.</p>
    <a class="card-btn">Read more</a>
  </article>
  <article class="abs card card--mind">
    <div class="card-icon" role="img" aria-label="Icon of a head with a brain"></div>
    <h3 class="card-title">Healthy Mind</h3>
    <p class="card-text">Itaque earum rerum hic tenetur a sapiente delectus, ut aut reiciendis voluptatibus maiores alias consequatur aut perferendis doloribus asperiores repellat.</p>
    <a class="card-btn">Read more</a>
  </article>

  <h2 class="abs section-title products-title">Our Products</h2>
  <p class="abs products-lead">Nam libero tempore, cum soluta nobis est eligendi optio cumque nihil<br>impedit quo minus id quod maxime placeat facere possimus,<br>omnis voluptas assumenda est, omnis dolor repellendus.</p>

  <section class="abs product product--orange">
    <div class="product-bottle" role="img" aria-label="Orange gummy vitamin bottle with green cap"></div>
    <h3 class="product-name">ORANGE</h3>
    <p class="product-tag">Shine and thrive</p>
    <p class="product-desc">Support healthy heart, brain, joint and eyes</p>
  </section>
  <section class="abs product product--elder">
    <div class="product-bottle" role="img" aria-label="Elderberry gummy vitamin bottle with purple cap"></div>
    <h3 class="product-name">ELDERBERRY</h3>
    <p class="product-tag">Set for adventure</p>
    <p class="product-desc">Immunity support</p>
  </section>
  <section class="abs product product--berry">
    <div class="product-bottle" role="img" aria-label="Strawberry gummy vitamin bottle with red cap"></div>
    <h3 class="product-name">STRAWBERRY</h3>
    <p class="product-tag">Born to explore</p>
    <p class="product-desc">Support your brain's learning, concentration and reasoning</p>
  </section>
  <a class="abs buy-btn buy-btn--orange">Buy now</a>
  <a class="abs buy-btn buy-btn--elder">Buy now</a>
  <a class="abs buy-btn buy-btn--berry">Buy now</a>

  <svg class="abs badges" width="592" height="74" viewBox="0 0 592 74" role="img" aria-label="Dietary certification badges">
    <g stroke="#ffffff" stroke-width="2" fill="none">
      <circle cx="35" cy="37" r="35" fill="var(--badge-1)"/><circle cx="35" cy="37" r="27"/>
      <circle cx="121" cy="37" r="35" fill="var(--badge-2)"/><circle cx="121" cy="37" r="27"/>
      <circle cx="209" cy="37" r="35" fill="var(--badge-3)"/><circle cx="209" cy="37" r="27"/>
      <circle cx="295" cy="37" r="35" fill="var(--badge-4)"/><circle cx="295" cy="37" r="27"/>
      <circle cx="383" cy="37" r="35" fill="var(--badge-5)"/><circle cx="383" cy="37" r="27"/>
      <circle cx="469" cy="37" r="35" fill="var(--badge-6)"/><circle cx="469" cy="37" r="27"/>
      <circle cx="557" cy="37" r="35" fill="var(--badge-7)"/><circle cx="557" cy="37" r="27"/>
    </g>
  </svg>
</main>

<footer class="abs contact">
  <div class="abs contact-frame"></div>
  <div class="abs contact-divider"></div>
  <div class="abs contact-col contact-col--phone">
    <div class="contact-icon">
      <svg width="30" height="30" viewBox="0 0 24 24" aria-hidden="true">
        <circle cx="12" cy="12" r="10.5" fill="none" stroke="#5bbde9" stroke-width="1.6"/>
        <path d="M8.6 6.8c.4-.3 1-.2 1.2.2l1 1.7c.2.4.1.8-.2 1.1l-.7.6c.5 1.2 1.4 2.2 2.6 2.7l.6-.7c.3-.3.8-.4 1.1-.2l1.7 1c.4.2.5.8.2 1.2l-.8 1c-.4.5-1.1.7-1.7.5-3.1-1-5.4-3.3-6.3-6.4-.2-.6 0-1.3.5-1.7z" fill="#5bbde9"/>
      </svg>
    </div>
    <p class="contact-note">Et harum quidem rerum facilis est et expedita distinctio.</p>
    <p class="contact-main">+62 (1) 9 8765 4321</p>
    <p class="contact-hours">MONDAY    -    SUNDAY</p>
    <p class="contact-time">08.00 AM    -    21.00 PM</p>
  </div>
  <div class="abs contact-col contact-col--mail">
    <div class="contact-icon">
      <svg width="30" height="24" viewBox="0 0 30 24" aria-hidden="true">
        <rect x="2" y="3" width="26" height="18" fill="none" stroke="#5bbde9" stroke-width="2"/>
        <path d="M2 3l13 10L28 3" fill="none" stroke="#5bbde9" stroke-width="2"/>
      </svg>
    </div>
    <p class="contact-note">Et harum quidem rerum facilis est et expedita distinctio.</p>
    <p class="contact-main">noreply@zestoplex.com</p>
    <p class="contact-hours">MONDAY    -    SUNDAY</p>
    <p class="contact-time">24 HOURS</p>
  </div>
</footer>

</body>
</html>
```